Centro Veterinário Solarena
Já é o terceiro serviço que contrato na plataforma e sempre sou bem atendida e fico muito satisfeita com os resultados!
Heitor, fiquei muito satisfeita com o seu suporte! Nos ajudou demais no alinhamento! Muitíssimo obrigada!

```html
<!DOCTYPE html>
<html lang="pt-BR">
<head>
<meta charset="UTF-8">
<title>Centro Veterinário Solarena – Assinatura</title>
<link href="https://fonts.googleapis.com/css2?family=Poppins:wght@300;400&display=swap" rel="stylesheet">
<style>
  :root {
    --page: #ffffff;
    --card: #f8f7f4;
    --navy: #1f2536;
    --text: #3f4147;
    --tan: #c8a07c;
    --faint: #efeeea;
  }
  html, body {
    margin: 0;
    width: 1200px;
    height: 1200px;
    overflow: hidden;
    background: var(--page);
  }
  .signature-card {
    position: absolute;
    left: 36px;
    top: 408px;
    width: 1128px;
    height: 340px;
    background: var(--card);
    border-radius: 48px 8px 48px 8px;
    box-shadow: 0 6px 18px rgba(0,0,0,0.18);
    overflow: hidden;
    font-family: "Poppins", sans-serif;
  }
  .decor-shape {
    position: absolute;
    left: 900px;
    top: 60px;
    width: 280px;
    height: 280px;
    border-radius: 50%;
    background: var(--faint);
    opacity: 0.6;
  }
  .brand-name {
    position: absolute;
    left: 64px;
    top: 0;
    height: 340px;
    width: 480px;
    display: flex;
    flex-direction: column;
    justify-content: center;
    margin: 0;
    color: var(--navy);
    font-weight: 300;
    font-size: 40px;
    line-height: 52px;
    letter-spacing: 1px;
  }
  .contacts {
    position: absolute;
    left: 600px;
    top: 48px;
    margin: 0;
    padding: 0;
    list-style: none;
    color: var(--text);
    font-size: 22px;
    line-height: 29px;
  }
  .contact {
    display: flex;
    align-items: flex-start;
    gap: 20px;
    margin-bottom: 18px;
  }
  .contact:last-child { margin-bottom: 0; }
  .contact svg {
    width: 26px;
    height: 26px;
    flex: none;
    fill: none;
    stroke: var(--tan);
    stroke-width: 1.8;
    stroke-linejoin: round;
    margin-top: 2px;
  }
</style>
</head>
<body>
  <section class="signature-card">
    <div class="decor-shape" role="img" aria-label="Forma decorativa suave ao fundo"></div>

    <h1 class="brand-name"><span>Centro Veterinário</span><span>Solarena</span></h1>

    <ul class="contacts">
      <li class="contact">
        <svg viewBox="0 0 24 24"><path d="M12 22s7-7.2 7-12.5A7 7 0 0 0 5 9.5C5 14.8 12 22 12 22z"/><circle cx="12" cy="9.5" r="2.5"/></svg>
        <span>Rua das Acácias, 1390<br>Jardim Aurora<br>Vila Solarena - BA</span>
      </li>
      <li class="contact">
        <svg viewBox="0 0 24 24"><path d="M5 4h4l2 5-2.5 1.5a11 11 0 0 0 5 5L15 13l5 2v4a1 1 0 0 1-1 1A16 16 0 0 1 4 5a1 1 0 0 1 1-1z"/></svg>
        <span>77 90000-4521</span>
      </li>
      <li class="contact">
        <svg viewBox="0 0 24 24"><rect x="3" y="5" width="18" height="14" rx="1.5"/><path d="M3.5 6l8.5 7 8.5-7"/></svg>
        <span>contato@cvsolarena.vet</span>
      </li>
      <li class="contact">
        <svg viewBox="0 0 24 24"><rect x="4" y="4" width="16" height="16" rx="2"/></svg>
        <span>@solarena.vet</span>
      </li>
      <li class="contact">
        <svg viewBox="0 0 24 24"><circle cx="12" cy="12" r="9"/><path d="M3 12h18M12 3c3 3 3 15 0 18M12 3c-3 3-3 15 0 18"/></svg>
        <span>www.cvsolarena.vet</span>
      </li>
    </ul>
  </section>
</body>
</html>
```